THE HOMESTEAD LEDGER
STATIONARY, ENVELOPES, FLYERS, BUSINESS CARDS
Project: THE HOMESTEAD LEDGER
THE HOMESTEAD LEDGER - Real Estate
Creative Brief
Professional
MALCOLM J. VANTREASE
PRINCIPAL BROKER
518 WILLOWCREST DRIVE ASHGROVE, TENNESSEE 37010
malcolmvantrease@quillmail.example
FRONT SIDE DESIGN AND/OR LOGO WITH INDIVIDUAL INFORMATION AND AREA FOR INDIVIDUAL PICTURE.
AT LEAST "THE HOMESTEAD LEDGER" LOGO. OPEN TO OTHER DESIGN AND/OR BORDERS WITH IT.

```html
<!DOCTYPE html>
<html lang="en">
<head>
<meta charset="utf-8">
<title>The Homestead Ledger – Business Cards</title>
<link href="https://fonts.googleapis.com/css2?family=Tinos:wght@400;700&display=swap" rel="stylesheet">
<style>
  :root {
    --backdrop: #5a3a24;
    --olive-light: #c9c08e;
    --olive: #a89d5f;
    --olive-dark: #8a7f45;
    --paper: #ffffff;
    --ink: #4a4a3c;
    --photo: #ffffff;
  }
  * { margin: 0; padding: 0; box-sizing: border-box; }
  html, body { width: 1200px; height: 732px; overflow: hidden; }
  body {
    background: var(--backdrop);
    font-family: "Tinos", "Times New Roman", serif;
    position: relative;
  }
  .card {
    position: absolute;
    width: 293px;
    height: 511px;
    box-shadow: 0 6px 14px rgba(0,0,0,0.45);
    overflow: hidden;
  }
  .card--olive {
    left: 89px; top: 84px;
    background: radial-gradient(ellipse at 50% 45%, var(--olive-light) 0%, var(--olive) 55%, var(--olive-dark) 100%);
  }
  .card--profile { left: 454px; top: 137px; background: var(--paper); }
  .card--white { left: 818px; top: 84px; background: var(--paper); }

  .brand {
    position: absolute;
    left: 0; right: 0;
    display: flex;
    align-items: center;
    justify-content: center;
    gap: 7px;
    color: var(--ink);
    font-weight: 700;
    font-size: 17px;
    letter-spacing: 0.5px;
    white-space: nowrap;
  }
  .brand__dot {
    width: 10px; height: 10px;
    border-radius: 50%;
    background: var(--ink);
    flex: none;
  }
  .card--olive .brand, .card--white .brand { top: 236px; }
  .card--profile .brand { top: 92px; }

  .profile__wave { position: absolute; left: 0; top: 0; }
  .profile__details {
    position: absolute;
    left: 0; right: 0; top: 238px;
    text-align: center;
    color: var(--paper);
  }
  .profile__name { font-size: 17px; font-weight: 400; letter-spacing: 0.5px; }
  .profile__title { font-size: 11px; letter-spacing: 0.5px; margin-top: 4px; }
  .profile__photo {
    position: absolute;
    left: 110px; top: 310px;
    width: 72px; height: 96px;
    background: var(--photo);
  }
  .profile__contact {
    position: absolute;
    left: 0; right: 0; top: 428px;
    text-align: center;
    color: var(--paper);
    font-size: 9px;
    font-style: normal;
    line-height: 15px;
    letter-spacing: 0.3px;
  }
</style>
</head>
<body>
  <section class="card card--olive" aria-label="Card front, olive">
    <div class="brand"><span class="brand__dot"></span>THE HOMESTEAD LEDGER</div>
  </section>

  <section class="card card--profile" aria-label="Card with broker details">
    <svg class="profile__wave" width="293" height="511" viewBox="0 0 293 511" aria-hidden="true">
      <defs>
        <radialGradient id="oliveFill" cx="50%" cy="55%" r="70%">
          <stop offset="0%" stop-color="#c9c08e"/>
          <stop offset="60%" stop-color="#a89d5f"/>
          <stop offset="100%" stop-color="#8a7f45"/>
        </radialGradient>
        <linearGradient id="silverBand" x1="0" y1="0" x2="1" y2="0">
          <stop offset="0%" stop-color="#eeeeee"/>
          <stop offset="50%" stop-color="#9a9a9a"/>
          <stop offset="100%" stop-color="#e6e6e6"/>
        </linearGradient>
      </defs>
      <path d="M0 186 C 90 206, 170 140, 293 152 L293 168 C 170 158, 90 222, 0 204 Z" fill="url(#silverBand)"/>
      <path d="M0 204 C 90 222, 170 158, 293 168 L293 511 L0 511 Z" fill="url(#oliveFill)"/>
    </svg>
    <div class="brand"><span class="brand__dot"></span>THE HOMESTEAD LEDGER</div>
    <div class="profile__details">
      <h1 class="profile__name">MALCOLM J. VANTREASE</h1>
      <p class="profile__title">PRINCIPAL BROKER</p>
    </div>
    <div class="profile__photo" role="img" aria-label="Area for broker portrait photo"></div>
    <address class="profile__contact">
      518 WILLOWCREST DRIVE<br>
      ASHGROVE, TENNESSEE 37010<br>
      cell: (615) 555-0148<br>
      e-mail: malcolmvantrease@quillmail.example
    </address>
  </section>

  <section class="card card--white" aria-label="Card front, white">
    <div class="brand"><span class="brand__dot"></span>THE HOMESTEAD LEDGER</div>
  </section>
</body>
</html>
```